BQL Groundworks & Freight Business Card

Can you please design a business card for an Earthworks, Haulage truck and machinery hire company. They also provide sand soil and mulch supply, as well as screening of products. Can you re-create the logo from the attached but add BQL Groundworks & Freight just use the three diamond design.

Target Market(s)

Earthmoving and Transport, Landscapers, Construction

Contact Information for Business Card

ABN 52 907 334 816, Doug Pelham, Managing Director, BQL Groundworks & Freight Mobile 0438 256 904 Email bqlfreight2010@mailvane.net

Font styles to use
Sans Serif

Colors
ec1f27
000000
cbcbcb
ffffff

Requirements
Must have
• Listed on the back, Earthworks | Haulage | Truck and Machinery Hire | Sand, Soil & Mulch Supply | Screening of Products
Nice to have
• Would be good for it to look appealing to a mans man, because it relates to heavy machinery, earthworks, construction etc. Black, red and white would be good maybe with a bit of silver somewhere.
Should not have
• not sure

```html
<!DOCTYPE html>
<html lang="en">
<head>
<meta charset="utf-8">
<title>BQL Groundworks &amp; Freight – Business Card</title>
<link rel="stylesheet" href="https://fonts.googleapis.com/css2?family=Lato:wght@400;700;900&display=swap">
<style>
  :root {
    --red: #ec1f27;
    --black: #000000;
    --silver: #cbcbcb;
    --silver-light: #d6d6d6;
    --white: #ffffff;
    --backdrop: #2b2b2b;
  }
  * { box-sizing: border-box; margin: 0; padding: 0; }
  html, body { width: 1200px; height: 1200px; overflow: hidden; }
  body {
    background: var(--backdrop);
    font-family: "Lato", sans-serif;
    position: relative;
  }
  .card {
    position: absolute;
    left: 220px;
    width: 760px;
    height: 434px;
    border-radius: 26px;
    overflow: hidden;
  }

  /* Back side */
  .card-back {
    top: 110px;
    background: var(--silver-light);
    border-bottom: 10px solid var(--red);
  }
  .brand {
    display: flex;
    align-items: center;
    gap: 14px;
  }
  .brand-square {
    background: var(--red);
    flex: none;
  }
  .brand-name {
    font-weight: 900;
    color: var(--black);
    letter-spacing: 0.5px;
  }
  .card-back .brand {
    position: absolute;
    top: 130px;
    left: 0; right: 0;
    justify-content: center;
  }
  .card-back .brand-square { width: 38px; height: 38px; }
  .card-back .brand-name { font-size: 36px; }
  .services {
    position: absolute;
    bottom: 34px;
    left: 0; right: 0;
    text-align: center;
    font-size: 19px;
    line-height: 1.35;
    color: var(--black);
  }

  /* Front side */
  .card-front {
    top: 640px;
    background: var(--white);
  }
  .card-front .brand {
    position: absolute;
    top: 52px;
    right: 44px;
  }
  .card-front .brand-square { width: 24px; height: 24px; }
  .card-front .brand-name { font-size: 22px; }
  .divider {
    position: absolute;
    top: 150px;
    left: 300px;
    right: 0;
    height: 2px;
    background: var(--red);
  }
  .person {
    position: absolute;
    top: 124px;
    left: 52px;
  }
  .person-name {
    font-size: 34px;
    font-weight: 900;
    color: var(--black);
    text-transform: uppercase;
    letter-spacing: -0.5px;
    line-height: 1;
  }
  .person-role {
    margin-top: 4px;
    font-size: 20px;
    font-weight: 700;
    color: var(--red);
    text-transform: uppercase;
  }
  .company {
    position: absolute;
    top: 240px;
    left: 90px;
    font-size: 20px;
    line-height: 1.25;
    color: var(--black);
  }
  .contact {
    position: absolute;
    top: 320px;
    left: 90px;
    list-style: none;
    font-size: 20px;
    color: var(--black);
  }
  .contact li {
    display: flex;
    align-items: center;
    gap: 14px;
    line-height: 1.4;
  }
  .contact svg { width: 18px; height: 18px; flex: none; }
</style>
</head>
<body>

<section class="card card-back" aria-label="Card back">
  <div class="brand">
    <span class="brand-square"></span>
    <span class="brand-name">BQL Groundworks &amp; Freight</span>
  </div>
  <p class="services">
    Earthworks | Haulage<br>
    Truck and Machinery Hire | Sand, Soil &amp; Mulch Supply | Screening of Products
  </p>
</section>

<section class="card card-front" aria-label="Card front">
  <div class="brand">
    <span class="brand-square"></span>
    <span class="brand-name">BQL Groundworks &amp; Freight</span>
  </div>
  <div class="divider"></div>
  <div class="person">
    <h1 class="person-name">Doug Pelham</h1>
    <p class="person-role">Managing Director</p>
  </div>
  <p class="company">
    ABN 52 907 334 816<br>
    BQL Groundworks &amp; Freight
  </p>
  <ul class="contact">
    <li>
      <svg viewBox="0 0 24 24" aria-hidden="true"><path fill="#ec1f27" d="M6.6 10.8a15 15 0 0 0 6.6 6.6l2.2-2.2c.3-.3.7-.4 1-.2 1.1.4 2.3.6 3.6.6.6 0 1 .4 1 1V20c0 .6-.4 1-1 1A17 17 0 0 1 3 4c0-.6.4-1 1-1h3.5c.6 0 1 .4 1 1 0 1.3.2 2.5.6 3.6.1.3 0 .7-.2 1z"/></svg>
      0438 256 904
    </li>
    <li>
      <svg viewBox="0 0 24 24" aria-hidden="true"><path fill="#ec1f27" d="M2 5h20v14H2z"/><path fill="none" stroke="#fff" stroke-width="1.8" d="M2.5 5.5 12 13l9.5-7.5"/></svg>
      bqlfreight2010@mailvane.net
    </li>
  </ul>
</section>

</body>
</html>
```